Veltracore Needs a Poster to Advertise a New Membership Offer

We need a Poster design for Veltracore Fitness Studio.
A first of it's kind membership, The Veltracore Fitness Studio combines the skills of our industry-leading Physiotherapists, Strength Coaches and Massage Therapists into one membership with a tailored plan to guide you through the fundamentals of Movement, Mobility and Recovery.
The concept is loosely based on the professional sports model, where every member of our team works together to produce lasting results for you. The final design should illustrate the bespoke nature of our program in a fun, supportive and professional space.
"Whether your aim is to be the best in the world, or the best in your world – it’s all the same to us."
Brand Guidelines
The poster should be on a black background and use our brand colour, lime green (hexcode #cefa08) as a highlight. Please don't overuse the highlight colour though. Generally, we opt for less bright colours and more of a 'street' look
Target Market(s)
The poster should attract predominantly female members, but should not exclude males. The target age range is 30-40 years female.
Industry/Entity Type
Health And Wellness
Font styles to use
Requirements
Must have
- Must Include
• VFS logo
• Tag line " Building Strong, Mobile, Bulletproof Humans"
• Call to action "Join us"
• Sized to 600(W)x900(H)mm
• Text: "A first of it's kind membership, The Veltracore Fitness Studio combines the skills of our industry-leading Physiotherapists, Strength Coaches and Massage Therapists into one membership with a tailored plan to guide you through the fundamentals of Movement, Mobility and Recovery."
Nice to have
- Ideal Inclusions
• Veltracore logo
• Text "Membership Now Open"
• Web address: veltracore.com.au
Should not have
- Don't Use:
• Too much of the highlight colour
• Cartoon imagery
• Images that are too staged or revealing (clothing). Image should fit our target market of everyday active people, not elite athletes or models.

```html
<!DOCTYPE html>
<html lang="en">
<head>
<meta charset="utf-8">
<title>Veltracore Fitness Studio – Membership Now Open</title>
<link rel="stylesheet" href="https://fonts.googleapis.com/css2?family=Anton&family=Montserrat:wght@500;600&display=swap">
<style>
  :root {
    --lime: #cefa08;
    --lime-soft: #c5dc2a;
    --ink: #151515;
    --white: #ffffff;
    --paper: #f4f6ee;
    --stage: #e9ecdf;
    --sky-top: #4f8fcf;
    --sky-mid: #9fbfd8;
    --sunset: #f08a3a;
    --ground: #3a3026;
  }
  * { box-sizing: border-box; margin: 0; padding: 0; }
  html, body { width: 1200px; height: 1200px; overflow: hidden; }
  body { background: var(--stage); position: relative; font-family: "Montserrat", sans-serif; }

  .poster {
    position: absolute; left: 240px; top: 60px;
    width: 720px; height: 1080px;
    background: var(--ink); overflow: hidden;
  }
  .poster__photo {
    position: absolute; left: 0; top: 0; width: 720px; height: 820px;
    background:
      linear-gradient(180deg, var(--sky-top) 0%, var(--sky-mid) 42%, #e7b98a 58%, var(--sunset) 66%, var(--ground) 74%, #2b241d 100%);
  }
  .poster__shapes { position: absolute; inset: 0; width: 720px; height: 1080px; }

  .brand-badge {
    position: absolute; left: 40px; top: 24px; width: 180px; height: 200px;
    background: var(--white); display: flex; align-items: center; justify-content: center;
  }
  .brand-badge__name { font-family: "Anton", sans-serif; font-size: 76px; color: var(--ink); letter-spacing: 1px; }

  .tagline {
    position: absolute; left: 250px; top: 92px; width: 440px;
    font-family: "Anton", sans-serif; font-size: 38px; line-height: 1.05;
    color: var(--white); text-transform: uppercase; letter-spacing: 0.5px;
  }

  .cta {
    position: absolute; left: 120px; top: 300px;
    font-family: "Anton", sans-serif; color: var(--white);
    font-size: 215px; line-height: 0.95; text-transform: uppercase;
    -webkit-text-stroke: 2px var(--lime-soft); paint-order: stroke fill;
    text-shadow: 4px 4px 0 rgba(0,0,0,0.25);
  }
  .cta__line { display: block; }
  .cta__line--second { padding-left: 70px; }

  .offer {
    position: absolute; left: 430px; top: 748px; width: 280px;
    font-family: "Anton", sans-serif; font-size: 46px; line-height: 1.02;
    color: var(--ink); text-transform: uppercase; text-align: center;
  }

  .about {
    position: absolute; left: 32px; top: 870px; width: 360px;
    color: var(--white); font-size: 16px; line-height: 1.45; font-weight: 500;
  }

  .signoff {
    position: absolute; left: 420px; top: 900px; width: 300px; text-align: center;
  }
  .signoff__name { font-family: "Montserrat", sans-serif; font-weight: 500; font-size: 42px; color: var(--ink); letter-spacing: -0.5px; }
  .signoff__web { font-size: 12px; letter-spacing: 5px; color: #8a9a2a; text-transform: uppercase; font-weight: 600; margin-top: 2px; }
</style>
</head>
<body>
  <main class="poster">
    <div class="poster__photo" role="img" aria-label="Photo of a woman running along a hillside track at sunset, sky fading from blue to orange"></div>

    <svg class="poster__shapes" viewBox="0 0 720 1080" aria-hidden="true">
      <polygon points="0,70 720,20 720,190 0,262" fill="#151515"/>
      <polygon points="0,262 720,190 720,206 0,282" fill="#c5dc2a"/>
      <polygon points="0,690 60,660 120,790 0,820" fill="#151515"/>
      <line x1="20" y1="660" x2="110" y2="800" stroke="#ffffff" stroke-width="4"/>
      <line x1="6" y1="700" x2="80" y2="810" stroke="#ffffff" stroke-width="3"/>
      <polygon points="0,820 420,780 420,1080 0,1080" fill="#151515"/>
      <polygon points="0,800 90,790 130,850 0,860" fill="#c5dc2a"/>
      <polygon points="420,740 720,700 720,880 420,880" fill="#c5dc2a"/>
      <polygon points="430,745 720,705" stroke="#151515" stroke-width="3" fill="none"/>
      <polygon points="420,880 720,880 720,1080 420,1080" fill="#f4f6ee"/>
    </svg>

    <div class="brand-badge"><span class="brand-badge__name">VFS</span></div>

    <h2 class="tagline">Building Strong, Mobile,<br>Bulletproof Humans</h2>

    <h1 class="cta"><span class="cta__line">Join</span><span class="cta__line cta__line--second">Us</span></h1>

    <p class="offer">Membership<br>Now Open</p>

    <p class="about">A first of it's kind membership, The Veltracore Fitness Studio combines the skills of our industry-leading Physiotherapists, Strength Coaches and Massage Therapists into one membership with a tailored plan to guide you through the fundamentals of Movement, Mobility and Recovery.</p>

    <div class="signoff">
      <div class="signoff__name">veltracore</div>
      <div class="signoff__web">veltracore.com.au</div>
    </div>
  </main>
</body>
</html>
```